Business card design needed

I need to display a copy of one of my paintings on front,
with my contact details displayed effectively within the painting.
On the back, my Logo needs to be displayed.
Font used should be artistic, but legible.
A high quality GLOSS Paper

Target Market(s)

Business people who purchase my Art for their premises and Boardrooms but also home owners both Traditional and Modern enthusiasts.

Industry/Entity Type

Business

Contact Information for Business Card

Artist /Interior Designer- Mellie Vantorski
Specializing in Oils on Canvas
Co-ordinate Colours in Home or Office
Over 25 years experience
mobile: 0492 581064
email: rowena.k@palvix.net.au
P.O. Box 518
Marlow Reach 2947 NSW

Requirements
Must have
• Good visual of painting, well proportioned.
Your can play with the description of Artist as long as it appeals to the above clientele.
Choose a painting which allows the potential client to see the text but showcases

the canvas too.

```html
<!DOCTYPE html>
<html lang="en">
<head>
<meta charset="utf-8">
<title>Mellie Vantorski Art – Business Card</title>
<link href="https://fonts.googleapis.com/css2?family=Cinzel:wght@400;500&family=Lora:ital,wght@1,400;1,700&display=swap" rel="stylesheet">
<style>
  :root {
    --page: #ffffff;
    --band: #2d2c2b;
    --band-logo: #1f1a12;
    --gold: #f5d21c;
    --gold-soft: #d9b64a;
    --text-light: #f2f0ec;
    --text-muted: #c9c4b8;
    --wisteria-dark: #1a1424;
    --wisteria-mid: #4f4c8f;
    --wisteria-light: #8b86c9;
    --leaf: #6f8f3a;
    --bark-pink: #e6c6d2;
    --bark-lilac: #c9c3e2;
    --bark-brown: #6b3d24;
  }
  html, body {
    margin: 0;
    padding: 0;
    background: var(--page);
  }
  .canvas {
    position: relative;
    width: 1200px;
    height: 1100px;
    overflow: hidden;
    background: var(--page);
  }
  .card {
    position: absolute;
    top: 135px;
    width: 451px;
    height: 810px;
    overflow: hidden;
  }
  .card--back { left: 93px; }
  .card--front { left: 606px; height: 805px; }

  .painting {
    position: absolute;
    left: 0;
    width: 100%;
  }
  .painting--wisteria {
    background:
      radial-gradient(ellipse at 30% 10%, rgba(170,170,200,0.55), transparent 45%),
      radial-gradient(ellipse at 20% 55%, var(--wisteria-light), transparent 40%),
      radial-gradient(ellipse at 75% 50%, var(--wisteria-mid), transparent 45%),
      radial-gradient(ellipse at 55% 80%, rgba(111,143,58,0.5), transparent 40%),
      linear-gradient(180deg, #3a3550 0%, var(--wisteria-dark) 100%);
  }
  .painting--branches {
    background:
      radial-gradient(ellipse at 40% 40%, rgba(107,61,36,0.55), transparent 35%),
      radial-gradient(ellipse at 80% 70%, rgba(107,61,36,0.45), transparent 35%),
      radial-gradient(ellipse at 20% 80%, var(--bark-lilac), transparent 50%),
      linear-gradient(160deg, var(--bark-lilac) 0%, var(--bark-pink) 50%, #d8b8c8 100%);
  }
  .card--back .painting--wisteria { top: 0; height: 380px; }
  .card--back .painting--branches { top: 450px; height: 360px; }
  .card--front .painting--wisteria { top: 0; height: 215px; }
  .card--front .painting--branches { top: 540px; height: 265px; }

  .logo-band {
    position: absolute;
    left: 0;
    top: 358px;
    width: 100%;
    height: 112px;
    background: linear-gradient(180deg, rgba(31,26,18,0.85) 0%, var(--band-logo) 40%, var(--band-logo) 75%, rgba(31,26,18,0.8) 100%);
    display: flex;
    flex-direction: column;
    justify-content: center;
    align-items: center;
    gap: 4px;
  }
  .logo-name {
    display: flex;
    align-items: center;
    gap: 8px;
    font-family: "Cinzel", serif;
    font-weight: 400;
    font-size: 24px;
    letter-spacing: 1px;
    color: var(--gold-soft);
  }
  .logo-mark {
    width: 10px;
    height: 10px;
    border-radius: 50%;
    background: var(--gold-soft);
  }
  .logo-tagline {
    font-family: "Cinzel", serif;
    font-size: 11px;
    letter-spacing: 1.4px;
    color: var(--text-muted);
    text-transform: uppercase;
  }

  .details-band {
    position: absolute;
    left: 0;
    top: 194px;
    width: 100%;
    height: 368px;
    background: linear-gradient(180deg, rgba(45,44,43,0.6) 0%, var(--band) 8%, var(--band) 92%, rgba(45,44,43,0.6) 100%);
    text-align: center;
    font-family: "Lora", serif;
    font-style: italic;
    color: var(--text-light);
  }
  .details-band p { margin: 0; position: absolute; left: 0; width: 100%; }
  .role { top: 38px; font-size: 21px; }
  .name {
    top: 64px;
    font-family: "Cinzel", serif;
    font-style: normal;
    font-size: 36px;
    letter-spacing: 1px;
    color: var(--gold);
  }
  .specialty { top: 126px; font-size: 18px; line-height: 25px; letter-spacing: 0.4px; }
  .experience { top: 182px; font-size: 21px; }
  .contact {
    font-weight: 700;
    color: var(--gold);
  }
  .contact--phone { top: 223px; font-size: 27px; display: flex; justify-content: center; align-items: center; gap: 6px; }
  .contact--email { top: 260px; font-size: 23px; }
  .phone-icon { width: 20px; height: 20px; }
  .address { top: 312px; font-size: 21px; letter-spacing: 0.3px; }
</style>
</head>
<body>
<main class="canvas">
  <section class="card card--back" aria-label="Card back with logo">
    <div class="painting painting--wisteria" role="img" aria-label="Oil painting of purple wisteria hanging from a grey branch"></div>
    <div class="painting painting--branches" role="img" aria-label="Oil painting of brown wisteria branches over pink and lilac tones"></div>
    <div class="logo-band">
      <div class="logo-name"><span>Mellie Vantorski Art</span><span class="logo-mark"></span></div>
      <div class="logo-tagline">Original Paintings for Home &amp; Office</div>
    </div>
  </section>

  <section class="card card--front" aria-label="Card front with contact details">
    <div class="painting painting--wisteria" role="img" aria-label="Oil painting of purple wisteria blossoms"></div>
    <div class="painting painting--branches" role="img" aria-label="Oil painting of twisting wisteria branches"></div>
    <div class="details-band">
      <p class="role">Artist /Interior Designer</p>
      <p class="name">MELLIE VANTORSKI</p>
      <p class="specialty">Specializing in Oils on Canvas<br>Co-ordinate Colours in Home or Office</p>
      <p class="experience">Over 25 years experience</p>
      <p class="contact contact--phone">
        <svg class="phone-icon" viewBox="0 0 24 24" aria-hidden="true"><path fill="#f5d21c" d="M6.6 10.8a15.1 15.1 0 0 0 6.6 6.6l2.2-2.2a1 1 0 0 1 1-.25 11.4 11.4 0 0 0 3.6.57 1 1 0 0 1 1 1V20a1 1 0 0 1-1 1A17 17 0 0 1 3 4a1 1 0 0 1 1-1h3.5a1 1 0 0 1 1 1c0 1.25.2 2.45.57 3.57a1 1 0 0 1-.25 1z"/></svg>
        <span>0492 581064</span>
      </p>
      <p class="contact contact--email">rowena.k@palvix.net.au</p>
      <p class="address">P.O. Box 518 Marlow Reach 2947 NSW</p>
    </div>
  </section>
</main>
</body>
</html>
```